Printed Promo Flyer for new pet business

We need a double sided flyer design as per the given example flyer, just better looking and more fun.Flyers will need to be printed.Flyer size approx 10.5cm x 15cm. The text will need to be amended slightly afterwards to be more fun unless you can create a new tone of voice as well (should sound fun like breezy do it) Look and Feel: emotional, fun, loving, professional
See attached files.

Target Market(s)

Pet owners in the UK who want the convenience of getting their pets parasite treatment delivered to their door without the need of having to run to the vet or store for purchase

Industry/Entity Type

Pet Care

Colors
00a990
6b449b

Requirements
Must have
• all the content context as given in the example flyer.
Nice to have
• Tone of voice can be changed to be more fun (using Breezy as a guide)

```html
<!DOCTYPE html>
<html lang="en">
<head>
<meta charset="utf-8">
<title>Happy Tail Bag – Flyer</title>
<link rel="stylesheet" href="https://fonts.googleapis.com/css2?family=Montserrat:wght@600;700;800&display=swap">
<style>
  :root{
    --purple:#603a7a;
    --teal:#2a9db0;
    --sky:#d6e6f1;
    --ink:#444448;
    --white:#ffffff;
  }
  html,body{margin:0;padding:0;width:1200px;height:865px;overflow:hidden;background:var(--white);}
  .flyer{position:absolute;top:173px;width:379px;height:536px;box-shadow:0 0 0 1px #eeeeee;}
  .flyer--front{left:221px;}
  .flyer--back{left:618px;}
  .flyer svg{display:block;width:100%;height:100%;}
  .t{font-family:'Montserrat',sans-serif;font-weight:800;}
  .t-semi{font-family:'Montserrat',sans-serif;font-weight:700;}
  .c-purple{fill:var(--purple);}
  .c-teal{fill:var(--teal);}
  .c-ink{fill:var(--ink);}
  .c-white{fill:var(--white);}
  .bg{fill:var(--sky);}
  .panel{fill:var(--white);}
  .frame{fill:none;stroke:var(--purple);stroke-width:14;stroke-linejoin:round;stroke-linecap:round;}
  .hex{fill:var(--white);stroke:var(--purple);stroke-width:14;stroke-linejoin:round;}
  .wave-teal{fill:var(--teal);}
  .wave-purple{fill:var(--purple);}
  .wave-white{fill:var(--white);}
  .tick-ring{fill:none;stroke:var(--purple);stroke-width:2.5;}
  .tick-mark{fill:none;stroke:var(--teal);stroke-width:3;stroke-linecap:round;stroke-linejoin:round;}
  .step-dot{fill:var(--purple);}
</style>
</head>
<body>

<!-- Front side -->
<div class="flyer flyer--front">
  <svg viewBox="0 0 716 1013" xmlns="http://www.w3.org/2000/svg">
    <defs>
      <linearGradient id="illoTone" x1="0" y1="0" x2="1" y2="1">
        <stop offset="0" stop-color="#f6dcb8"/>
        <stop offset="1" stop-color="#efb27a"/>
      </linearGradient>
    </defs>
    <rect class="bg" width="716" height="1013"/>

    <path class="panel" d="M0 0 H570 L625 262 Q632 300 605 330 L360 540 Q330 563 290 552 L0 460 Z"/>
    <path class="frame" d="M0 460 L290 552 Q330 563 360 540 L605 330 Q632 300 625 262 L570 0"/>

    <rect role="img" aria-label="Illustration of a puppy with a flea under a magnifying glass" x="430" y="20" width="130" height="110" rx="10" fill="url(#illoTone)"/>
    <rect role="img" aria-label="Illustration of a winking dog scratching, flea under a magnifying glass" x="385" y="150" width="195" height="150" rx="10" fill="url(#illoTone)"/>
    <rect role="img" aria-label="Illustration of a ginger cat scratching with a magnified flea" x="0" y="262" width="240" height="165" rx="10" fill="url(#illoTone)"/>
    <rect role="img" aria-label="Illustration of a dog scratching with a magnified flea" x="252" y="325" width="172" height="125" rx="10" fill="url(#illoTone)"/>

    <path class="hex" d="M15 0 L65 175 Q75 205 110 215 L250 245 Q275 250 295 232 L405 125 Q420 108 415 85 L395 0"/>
    <text class="t c-purple" x="215" y="135" font-size="44" text-anchor="middle">HAPPY TAIL</text>
    <text class="t c-purple" x="215" y="180" font-size="44" text-anchor="middle">BAG</text>

    <polygon class="hex" points="555,450 683,518 683,622 555,690 428,622 428,518"/>
    <text x="555" y="548" text-anchor="middle"><tspan class="t c-teal" font-size="24">THE </tspan><tspan class="t c-purple" font-size="36">BEST</tspan></text>
    <text class="t c-purple" x="555" y="584" font-size="31" text-anchor="middle">PROTECTION</text>
    <text class="t c-teal" x="555" y="607" font-size="19" text-anchor="middle">AND</text>
    <text class="t c-purple" x="557" y="643" font-size="32" text-anchor="middle">CARE</text>

    <text class="t c-teal" x="42" y="755" font-size="120" letter-spacing="-2">FOR</text>
    <text class="t c-purple" x="42" y="845" font-size="88" letter-spacing="-2">YOUR PET</text>

    <path class="wave-teal" d="M140 1013 L145 965 Q165 950 205 944 L590 858 Q615 852 640 866 L716 910 V1013 Z"/>
    <path class="wave-purple" d="M0 1013 V975 L590 884 Q618 879 645 895 L716 938 V1013 Z"/>
    <path class="wave-white" d="M110 1013 Q128 970 180 962 L590 902 Q615 897 640 911 L716 958 V1013 Z"/>
    <text class="t c-ink" x="565" y="960" font-size="22" text-anchor="middle">WITH</text>
    <text class="t c-ink" x="670" y="992" font-size="30" text-anchor="end">HAPPY TAIL BAG</text>
  </svg>
</div>

<!-- Back side -->
<div class="flyer flyer--back">
  <svg viewBox="0 0 716 1013" xmlns="http://www.w3.org/2000/svg">
    <defs>
      <linearGradient id="photoTone" x1="1" y1="0" x2="0" y2="1">
        <stop offset="0" stop-color="#4f7fb5"/>
        <stop offset="0.45" stop-color="#c9d3dc"/>
        <stop offset="0.75" stop-color="#eef0f2"/>
        <stop offset="1" stop-color="#8a8d92"/>
      </linearGradient>
    </defs>
    <rect class="bg" width="716" height="1013"/>

    <path role="img" aria-label="Photo of a vet combing a fluffy dog lying on its back" fill="url(#photoTone)" d="M0 0 H565 L625 262 Q632 300 605 330 L400 530 Q370 556 330 548 L0 460 Z"/>
    <path class="frame" d="M0 460 L330 548 Q370 556 400 530 L605 330 Q632 300 625 262 L565 0"/>

    <path class="hex" d="M15 0 L60 130 Q70 160 105 168 L210 190 Q235 195 255 178 L330 105 Q345 90 340 68 L325 0"/>
    <text class="t c-purple" x="175" y="100" font-size="34" text-anchor="middle">HAPPY TAIL</text>
    <text class="t c-purple" x="175" y="136" font-size="34" text-anchor="middle">BAG</text>

    <text class="t c-teal" x="105" y="482" font-size="52">FOR</text>
    <text class="t c-purple" x="185" y="518" font-size="38">YOUR PET</text>

    <polygon class="hex" points="593,398 690,448 690,540 593,590 496,540 496,448"/>
    <text class="t c-purple" x="508" y="496" font-size="72">£</text>
    <text class="t c-purple" x="555" y="458" font-size="19">FIRST BOX</text>
    <text class="t c-teal" x="553" y="500" font-size="50">5.99</text>
    <text class="t c-ink" x="555" y="528" font-size="19">USE CODE</text>
    <rect x="544" y="533" width="106" height="20" fill="var(--teal)"/>
    <text class="t c-white" x="597" y="549" font-size="16" text-anchor="middle">XXX</text>

    <text class="t c-teal" x="22" y="602" font-size="32">WHY HAPPY TAIL BAG</text>

    <g transform="translate(36,640)"><circle class="tick-ring" r="10"/><path class="tick-mark" d="M-5 0 L-1 5 L9 -8"/></g>
    <text class="t c-ink" x="58" y="648" font-size="26">PROTECTION &amp; CARE</text>
    <text class="t-semi c-ink" x="58" y="667" font-size="11">Protection against all major parasites to avoid</text>
    <text class="t-semi c-ink" x="58" y="683" font-size="11">putting your pet and your family at risk.</text>

    <g transform="translate(36,720)"><circle class="tick-ring" r="10"/><path class="tick-mark" d="M-5 0 L-1 5 L9 -8"/></g>
    <text class="t c-ink" x="58" y="728" font-size="26">IN TIME</text>
    <text class="t-semi c-ink" x="58" y="747" font-size="11">Never having to remember when to treat your pet.</text>

    <g transform="translate(36,798)"><circle class="tick-ring" r="10"/><path class="tick-mark" d="M-5 0 L-1 5 L9 -8"/></g>
    <text class="t c-ink" x="58" y="806" font-size="26">CONVENIENT</text>
    <text class="t-semi c-ink" x="58" y="825" font-size="11">Delivered directly to your letter box.</text>

    <g transform="translate(36,858)"><circle class="tick-ring" r="10"/><path class="tick-mark" d="M-5 0 L-1 5 L9 -8"/></g>
    <text class="t c-ink" x="58" y="866" font-size="26">LOW COST</text>
    <text class="t-semi c-ink" x="58" y="886" font-size="11">All the high end, trusted brands but cheaper than</text>
    <text class="t-semi c-ink" x="58" y="902" font-size="11">the vet.</text>

    <text class="t c-purple" x="418" y="651" font-size="29">HOW IT WORKS</text>
    <g class="t c-white" font-size="12" text-anchor="middle">
      <circle class="step-dot" cx="428" cy="684" r="9"/><text x="428" y="688">1</text>
      <circle class="step-dot" cx="428" cy="729" r="9"/><text x="428" y="733">2</text>
      <circle class="step-dot" cx="428" cy="770" r="9"/><text x="428" y="774">3</text>
      <circle class="step-dot" cx="428" cy="815" r="9"/><text x="428" y="819">4</text>
    </g>
    <g class="t-semi c-ink" font-size="14">
      <text x="450" y="688">Select which pet the</text>
      <text x="450" y="704">treatment is for.</text>
      <text x="450" y="734">Choose your treatment type.</text>
      <text x="448" y="775">Select your preferred brand.</text>
      <text x="450" y="819">Choose between 1,3,6 or 12</text>
      <text x="450" y="835">months treatment box.</text>
    </g>

    <path class="wave-teal" d="M140 1013 L145 965 Q165 950 205 944 L590 858 Q615 852 640 866 L716 910 V1013 Z"/>
    <path class="wave-purple" d="M0 1013 V975 L590 884 Q618 879 645 895 L716 938 V1013 Z"/>
    <path class="wave-white" d="M110 1013 Q128 970 180 962 L590 902 Q615 897 640 911 L716 958 V1013 Z"/>
    <text class="t c-ink" x="680" y="992" font-size="28" text-anchor="end">www.happytailbag.co.uk</text>
  </svg>
</div>

</body>
</html>
```